Supermarket Business Card Design
Pellman's Supermarket
Use standard fonts
Tobias Pellman
President
478 Linden Ave.
Brookfield, VT 05036
tpellman@pellmansupermarket.com
This is the logo I would like in the business card
Here is the logo in AI format but I want the logo on the left to be used

```html
<!DOCTYPE html>
<html lang="en">
<head>
<meta charset="UTF-8">
<title>Pellman's Supermarket – Business Card</title>
<link href="https://fonts.googleapis.com/css2?family=Cinzel:wght@400;600&display=swap" rel="stylesheet">
<style>
  :root {
    --backdrop: #e9e6e1;
    --card: #ffffff;
    --brand-red: #b5121b;
    --ink: #3a3a3a;
    --icon: #4a4a4a;
  }
  * { margin: 0; padding: 0; box-sizing: border-box; }
  html, body {
    width: 1200px;
    height: 914px;
    overflow: hidden;
    background: var(--backdrop);
    font-family: "Cinzel", serif;
  }
  .card {
    position: absolute;
    left: 75px;
    top: 157px;
    width: 1050px;
    height: 600px;
    background: var(--card);
    box-shadow: 0 6px 24px rgba(0,0,0,0.12);
  }
  .brand {
    position: absolute;
    top: 170px;
    left: 0;
    width: 100%;
    display: flex;
    justify-content: center;
    align-items: center;
    gap: 18px;
  }
  .brand-dot {
    width: 80px;
    height: 80px;
    border-radius: 50%;
    background: var(--brand-red);
  }
  .brand-name {
    color: var(--brand-red);
    font-weight: 600;
    font-size: 36px;
    letter-spacing: 1px;
    line-height: 1;
  }
  .holder {
    position: absolute;
    top: 318px;
    left: 0;
    width: 100%;
    text-align: center;
    color: var(--brand-red);
    font-size: 21px;
    letter-spacing: 1px;
  }
  .contacts {
    position: absolute;
    top: 385px;
    left: 170px;
    right: 120px;
    color: var(--ink);
    font-size: 16px;
    letter-spacing: 0.4px;
  }
  .contact-row {
    display: flex;
    align-items: center;
    gap: 10px;
    height: 36px;
  }
  .contact-row.phone { padding-left: 80px; }
  .contact-row.split { padding-left: 110px; justify-content: space-between; }
  .contact-item { display: flex; align-items: center; gap: 10px; }
  .icon { width: 18px; height: 18px; flex: none; }
</style>
</head>
<body>
  <section class="card">
    <div class="brand">
      <span class="brand-dot"></span>
      <span class="brand-name">PELLMAN'S SUPERMARKET</span>
    </div>

    <p class="holder">Tobias Pellman / President</p>

    <div class="contacts">
      <div class="contact-row">
        <svg class="icon" viewBox="0 0 20 20" aria-hidden="true">
          <circle cx="10" cy="10" r="10" fill="var(--icon)"/>
          <path d="M10 4.5a3.5 3.5 0 0 0-3.5 3.5c0 2.6 3.5 7 3.5 7s3.5-4.4 3.5-7A3.5 3.5 0 0 0 10 4.5zm0 4.8a1.3 1.3 0 1 1 0-2.6 1.3 1.3 0 0 1 0 2.6z" fill="#fff"/>
        </svg>
        <span>478 Linden Ave. Brookfield, VT 05036</span>
      </div>
      <div class="contact-row phone">
        <svg class="icon" viewBox="0 0 20 20" aria-hidden="true">
          <circle cx="10" cy="10" r="10" fill="var(--icon)"/>
          <path d="M7 5l2 2.5-1.2 1.3a7 7 0 0 0 3.4 3.4l1.3-1.2L15 13l-1 2c-4.5 0-9-4.5-9-9z" fill="#fff"/>
        </svg>
        <span>802.555.0187</span>
      </div>
      <div class="contact-row split">
        <div class="contact-item">
          <svg class="icon" viewBox="0 0 20 20" aria-hidden="true">
            <circle cx="10" cy="10" r="10" fill="var(--icon)"/>
            <rect x="5" y="6.5" width="10" height="7" fill="none" stroke="#fff" stroke-width="1.2"/>
            <path d="M5 6.5l5 4 5-4" fill="none" stroke="#fff" stroke-width="1.2"/>
          </svg>
          <span>tpellman@pellmansupermarket.com</span>
        </div>
        <div class="contact-item">
          <svg class="icon" viewBox="0 0 20 20" aria-hidden="true">
            <circle cx="10" cy="10" r="10" fill="var(--icon)"/>
            <circle cx="10" cy="10" r="5" fill="none" stroke="#fff" stroke-width="1.2"/>
            <path d="M5 10h10M10 5c-2 2.5-2 7.5 0 10M10 5c2 2.5 2 7.5 0 10" fill="none" stroke="#fff" stroke-width="1"/>
          </svg>
          <span>www.pellmansupermarket.com</span>
        </div>
      </div>
    </div>
  </section>
</body>
</html>
```